Simple display banner tension fabric design for a real estate development

Hello my friend,
I need from you a very professional display banner tension fabric design for my real estate development.

I need ready to print source files (standard bleed for display banners added)
I tried a lot to make it by myself but I don't like the results.

Please find attached my ugly design. Please copy/paste the content/text over your new design.

Display banner popup details:

Dimensions:

Content
- 315cm width x210(height)cm

Content + bleed
- 335cm width x238(height)cm

Link from where I buy the display banner:
- http://www.panourimobilevest.eu/popup_display_tension_fabric.html

Text/Content for copy/paste:

Header: "Cel mai nou complex rezidențial din Cluj, Apahida."

Main left: "74 de case, comunitate închisă, locuri de joacă pentru copii, curte cu gazon, 2 locuri de parcare"

Footer right: "open space living și bucătărie, 3 dormitoare, 3 băi, 119mp locuibili, parcele de teren 250-350mp"

Specification:

1. Minimalist design.
2. Clean design.
3. Competitive.

Fell free to google search any amazing ideas for this job.

In the attachements you find:

1. Logo
2. Images
3. My ugly design

I will give a bonus of 50 USD if the banner is beyond the limits.

Thank you,
Mirel.

```html
<!DOCTYPE html>
<html lang="ro">
<head>
<meta charset="utf-8">
<title>Livada Verde Residence – banner</title>
<link href="https://fonts.googleapis.com/css2?family=Roboto+Condensed:wght@400;700&family=Raleway:wght@400&display=swap" rel="stylesheet">
<style>
  :root {
    --green: #3daa47;
    --green-dark: #1f7f34;
    --green-deep: #166a2a;
    --green-light: #74c56f;
    --green-pale: #a9dca2;
    --white: #ffffff;
    --room-warm: #cdbba3;
    --room-light: #e9e6e1;
    --photo-house: #b9c6cf;
    --photo-kitchen: #e6e1da;
    --photo-bedroom: #d8ccc0;
  }
  * { margin: 0; padding: 0; box-sizing: border-box; }
  html, body { width: 1200px; height: 811px; overflow: hidden; background: #f2f2f2; }
  .banner {
    position: relative; width: 1200px; height: 811px; overflow: hidden;
    font-family: "Roboto Condensed", "Arial Narrow", sans-serif; color: var(--white);
  }
  .interior-photo {
    position: absolute; left: 0; top: 100px; width: 1200px; height: 540px;
    background: linear-gradient(100deg, var(--room-warm) 0%, var(--room-light) 45%, #f4f1ec 65%, #8a6f60 100%);
  }
  .header-band { position: absolute; left: 0; top: 0; width: 1200px; height: 160px; }
  .brand {
    position: absolute; left: 40px; top: 52px;
    display: flex; align-items: center; gap: 12px;
    font-family: "Raleway", sans-serif; font-weight: 400; color: var(--white);
  }
  .brand-mark { width: 14px; height: 14px; background: var(--white); flex: none; }
  .brand-name { display: flex; flex-direction: column; align-items: center; line-height: 1; }
  .brand-name-main { font-size: 28px; letter-spacing: .3px; }
  .brand-name-sub { font-size: 11px; letter-spacing: 4px; margin-top: 5px; }
  .headline {
    position: absolute; left: 360px; top: 86px;
    font-weight: 700; font-size: 36px; line-height: 44px; letter-spacing: .2px;
    white-space: nowrap;
    text-shadow: 0 1px 2px rgba(0,0,0,.25);
  }
  .features-panel {
    position: absolute; left: 0; top: 200px; width: 440px; height: 200px;
    background: rgba(61,170,71,.72); padding: 22px 0 0 62px;
  }
  .features-panel li, .specs-panel li { list-style: none; display: flex; align-items: center; }
  .features-panel li { font-weight: 700; font-size: 26px; line-height: 33px; gap: 12px; }
  .bullet { width: 20px; height: 20px; flex: none; }
  .specs-panel {
    position: absolute; left: 845px; top: 455px; width: 330px; height: 130px;
    background: var(--green); padding: 18px 0 0 24px; border-radius: 0 0 0 40px;
  }
  .specs-panel li { font-size: 15px; line-height: 20px; gap: 8px; }
  .specs-panel li::before { content: ""; width: 6px; height: 6px; border-radius: 50%; background: var(--white); }
  .footer-waves { position: absolute; left: 0; top: 0; width: 1200px; height: 811px; }
  .photo-circle {
    position: absolute; border-radius: 50%; border: 12px solid var(--green-dark);
    box-shadow: 0 0 0 4px var(--green-light);
  }
  .photo-house { left: 55px; top: 510px; width: 190px; height: 190px; background: linear-gradient(180deg, #9ec1d9 0%, var(--photo-house) 45%, #6e8f5a 100%); }
  .photo-kitchen { left: 305px; top: 505px; width: 190px; height: 190px; background: linear-gradient(180deg, #f7f6f3 0%, var(--photo-kitchen) 55%, #c9a77d 100%); }
  .photo-bedroom { left: 555px; top: 525px; width: 170px; height: 170px; background: linear-gradient(160deg, #f1ede8 0%, var(--photo-bedroom) 55%, #8e7d70 100%); }
  .website {
    position: absolute; right: 40px; top: 720px;
    font-weight: 700; font-size: 22px; letter-spacing: .3px;
  }
</style>
</head>
<body>
<div class="banner">
  <div class="interior-photo" role="img" aria-label="Open-plan living room and kitchen interior with grey sofa, cushions, bar stools and pendant lights"></div>

  <svg class="header-band" viewBox="0 0 1200 160" preserveAspectRatio="none" aria-hidden="true">
    <path d="M0 0 H1200 V140 H1010 C900 140 860 155 760 155 H0 Z" fill="var(--green)"/>
    <path d="M0 125 C300 155 600 120 760 155 H0 Z" fill="var(--green-dark)" opacity=".35"/>
  </svg>
  <div class="brand">
    <span class="brand-mark"></span>
    <span class="brand-name">
      <span class="brand-name-main">Livada Verde</span>
      <span class="brand-name-sub">RESIDENCE</span>
    </span>
  </div>
  <h1 class="headline">Cel mai nou complex rezidențial din Cluj, Apahida.</h1>

  <ul class="features-panel">
    <li><svg class="bullet" viewBox="0 0 20 20"><circle cx="10" cy="10" r="9" fill="var(--white)"/><path d="M6 10 H13 M10 7 L13 10 L10 13" stroke="var(--green-dark)" stroke-width="2" fill="none"/></svg>74 de case</li>
    <li><svg class="bullet" viewBox="0 0 20 20"><circle cx="10" cy="10" r="9" fill="var(--white)"/><path d="M6 10 H13 M10 7 L13 10 L10 13" stroke="var(--green-dark)" stroke-width="2" fill="none"/></svg>comunitate închisă</li>
    <li><svg class="bullet" viewBox="0 0 20 20"><circle cx="10" cy="10" r="9" fill="var(--white)"/><path d="M6 10 H13 M10 7 L13 10 L10 13" stroke="var(--green-dark)" stroke-width="2" fill="none"/></svg>locuri de joacă pentru copii</li>
    <li><svg class="bullet" viewBox="0 0 20 20"><circle cx="10" cy="10" r="9" fill="var(--white)"/><path d="M6 10 H13 M10 7 L13 10 L10 13" stroke="var(--green-dark)" stroke-width="2" fill="none"/></svg>curte cu gazon</li>
    <li><svg class="bullet" viewBox="0 0 20 20"><circle cx="10" cy="10" r="9" fill="var(--white)"/><path d="M6 10 H13 M10 7 L13 10 L10 13" stroke="var(--green-dark)" stroke-width="2" fill="none"/></svg>2 locuri de parcare</li>
  </ul>

  <svg class="footer-waves" viewBox="0 0 1200 811" preserveAspectRatio="none" aria-hidden="true">
    <path d="M0 600 C300 560 700 640 1200 570 V811 H0 Z" fill="var(--green-light)"/>
    <path d="M0 625 C350 590 750 660 1200 600 V811 H0 Z" fill="var(--green)"/>
    <path d="M0 700 C350 660 800 740 1200 680 V811 H0 Z" fill="var(--green-dark)" opacity=".45"/>
    <path d="M0 760 C400 720 800 790 1200 740" stroke="var(--green-pale)" stroke-width="3" fill="none" opacity=".6"/>
  </svg>

  <ul class="specs-panel">
    <li>open space living și bucătărie</li>
    <li>3 dormitoare</li>
    <li>3 băi</li>
    <li>119mp locuibili</li>
    <li>parcele de teren 250-350mp</li>
  </ul>

  <div class="photo-circle photo-house" role="img" aria-label="Exterior of a two-storey white residential house with garden"></div>
  <div class="photo-circle photo-kitchen" role="img" aria-label="Bright white kitchen with dining table"></div>
  <div class="photo-circle photo-bedroom" role="img" aria-label="Cosy bedroom corner with sofa and framed pictures"></div>

  <div class="website">www.livadaverde.ro</div>
</div>
</body>
</html>
```